Need cover for book about the Silk Traps child sex traffickers play with their victims

We train professionals, first responders, parents, foster parents, and others about child sex trafficking in the United States. This book is based on the life story of a former 32-year child sex trafficker who sold more than 150 children and women in all 50 states, Canada, and Europe. The book will not only help prevent kids from becoming victims of people like he was, but it also will prevent youth from becoming traffickers, as well.

```html
<!DOCTYPE html>
<html lang="en">
<head>
<meta charset="utf-8">
<title>Silk Traps — Book Cover</title>
<link href="https://fonts.googleapis.com/css2?family=Bebas+Neue&family=PT+Sans&display=swap" rel="stylesheet">
<style>
  :root {
    --ink: #0d0d0d;
    --paper: #ffffff;
    --backdrop: #ebebeb;
    --text-soft: #1a1a1a;
  }
  html, body {
    margin: 0;
    padding: 0;
    width: 1200px;
    height: 675px;
    overflow: hidden;
    background: var(--backdrop);
  }
  .stage {
    position: relative;
    width: 1200px;
    height: 675px;
  }
  .cover {
    position: absolute;
    left: 375px;
    top: 0;
    width: 450px;
    height: 675px;
    background: var(--paper);
    color: var(--ink);
  }
  .cover-title {
    position: absolute;
    left: 0;
    top: 0;
    width: 450px;
    height: 400px;
  }
  .cover-title text {
    font-family: "Bebas Neue", "Arial Narrow", sans-serif;
    fill: var(--ink);
  }
  .figure-slot {
    fill: var(--ink);
  }
  .subtitle {
    position: absolute;
    left: 0;
    width: 450px;
    top: 442px;
    margin: 0;
    text-align: center;
    font-family: "Bebas Neue", "Arial Narrow", sans-serif;
    font-weight: 400;
    font-size: 30px;
    line-height: 29px;
    letter-spacing: 1px;
    transform: rotate(-3deg);
    transform-origin: 225px 29px;
  }
  .credits {
    position: absolute;
    left: 0;
    width: 450px;
    top: 566px;
    text-align: center;
  }
  .authors {
    margin: 0;
    font-family: "Bebas Neue", "Arial Narrow", sans-serif;
    font-size: 26px;
    line-height: 24px;
    letter-spacing: 0.3px;
  }
  .authors .note {
    font-size: 12.5px;
    letter-spacing: 0.2px;
  }
  .foreword {
    margin: 3px 0 0;
    font-family: "PT Sans", Arial, sans-serif;
    font-size: 10px;
    line-height: 13px;
    color: var(--text-soft);
  }
</style>
</head>
<body>
<main class="stage">
  <article class="cover">
    <svg class="cover-title" viewBox="0 0 450 400" aria-labelledby="title-text">
      <title id="title-text">Silk Traps</title>
      <g class="title-line title-line--silk">
        <text x="41" y="234" font-size="247" textLength="100" lengthAdjust="spacingAndGlyphs">S</text>
        <rect class="figure-slot" x="160" y="42" width="58" height="192" role="img" aria-label="Silhouette of a man in a fedora leaning in place of the letter I"/>
        <text x="232" y="234" font-size="247" textLength="82" lengthAdjust="spacingAndGlyphs">L</text>
        <text x="326" y="234" font-size="247" textLength="88" lengthAdjust="spacingAndGlyphs">K</text>
      </g>
      <g class="title-line title-line--traps">
        <text x="30" y="381" font-size="201" textLength="70" lengthAdjust="spacingAndGlyphs">T</text>
        <text x="108" y="381" font-size="201" textLength="74" lengthAdjust="spacingAndGlyphs">R</text>
        <text x="190" y="381" font-size="201" textLength="82" lengthAdjust="spacingAndGlyphs">A</text>
        <text x="280" y="381" font-size="201" textLength="70" lengthAdjust="spacingAndGlyphs">P</text>
        <text x="358" y="381" font-size="201" textLength="62" lengthAdjust="spacingAndGlyphs">S</text>
      </g>
    </svg>

    <h2 class="subtitle">Exposing Recruiter<br>Manipulation Tactics</h2>

    <section class="credits">
      <p class="authors">Dr. Renata Hale &amp;<br>Marcus Doyle <span class="note">(a former 32-year child sex trafficker)</span></p>
      <p class="foreword">With forward by Lena Doyle, Marcus’s longtime victim and bottom and<br>creator of the Open Doors, New Paths program</p>
    </section>
  </article>
</main>
</body>
</html>
```